Business and Discussion forum website

I have long been an admirer of a good and professional business forum. Http://lanternboards.example got my attention and i am looking for a similar website to it. Basically, my website is going to discuss business, politics, entertainment and social issues. The website should be youthful and captivating. Users should be able to post threads, comments on threads, like and dislike comments. The administrator of the website will be able to delete post/threads. Users should be able to add each other as friends and subsequently be able to message/inbox each other. These are the basic stuffs the website should possess.

Industry/Entity Type

Business

Coding

Coded - Design and coding required

```html
<!DOCTYPE html>
<html lang="en">
<head>
<meta charset="utf-8">
<title>Lantern Boards</title>
<link href="https://fonts.googleapis.com/css2?family=Montserrat:wght@400;500;600;700;800&display=swap" rel="stylesheet">
<style>
:root{
  --navy:#2f2e66;
  --red:#d21f1f;
  --ink:#3a3a4a;
  --muted:#666672;
  --line:#ececf0;
  --white:#ffffff;
}
*{margin:0;padding:0;box-sizing:border-box}
html,body{width:699px;height:1200px;overflow:hidden;background:var(--white)}
body{font-family:"Montserrat",Arial,sans-serif;color:var(--ink);position:relative}
.page{position:relative;width:699px;height:1200px}

/* hero */
.hero{position:absolute;left:0;top:0;width:699px;height:324px;overflow:hidden}
.hero-photo{position:absolute;inset:0;background:
  radial-gradient(ellipse 120px 160px at 330px 200px,#3a2a32 0%,#1b1a2c 60%,transparent 100%),
  linear-gradient(90deg,#2b2a7a 0%,#16152a 25%,#121220 50%,#1a1838 75%,#2d2b80 100%)}
.brand{position:absolute;left:100px;top:25px;font-size:17px;font-weight:700;color:var(--white);letter-spacing:.2px;white-space:nowrap}
.nav{position:absolute;top:27px;left:0;width:699px;height:20px}
.nav a{position:absolute;font-size:8.5px;font-weight:700;color:var(--white);text-decoration:none;white-space:nowrap}
.nav a.active::after{content:"";position:absolute;left:-6px;right:-6px;top:15px;height:2px;background:var(--red)}
.arrow{position:absolute;top:161px;width:14px;height:16px}
.search{position:absolute;left:144px;top:214px;width:411px;height:43px;display:flex}
.search-field{flex:1;background:var(--white);font-size:6.5px;color:#777;padding:0 14px;display:flex;align-items:center}
.search-btn{width:96px;background:var(--red);color:var(--white);font-size:8px;font-weight:700;display:flex;align-items:center;justify-content:center}

/* section titles */
.section-title{position:absolute;left:0;width:699px;text-align:center;font-size:14px;font-weight:700;color:var(--navy)}

/* categories */
.card{position:absolute;top:394px;width:115px;height:192px;border:1px solid var(--line);background:var(--white)}
.card-photo{position:absolute;left:6px;top:9px;width:101px;height:73px}
.card-title{position:absolute;left:6px;top:99px;font-size:8px;font-weight:700;color:var(--red);display:flex;align-items:center;gap:5px;white-space:nowrap}
.card-title svg{width:8px;height:8px}
.bullets{list-style:none;position:absolute}
.bullets li{font-size:6.3px;color:var(--ink);height:14px;position:relative;padding-left:13px;white-space:nowrap}
.bullets li::before{content:"›";position:absolute;left:0;top:-2px;color:var(--red);font-size:8px}
.card .bullets{left:6px;top:119px}

/* link bands */
.band{position:absolute;top:622px;width:242px;height:36px;color:var(--white);font-size:10.5px;font-weight:700;display:flex;align-items:center;padding-left:14px}
.band.popular{left:102px;background:var(--navy)}
.band.recent{left:356px;background:var(--red)}
.links .bullets{top:679px}
.links .bullets li{height:14px}

/* news */
.news{position:absolute;top:846px;width:157px}
.news-photo{width:157px;height:96px}
.news-date{margin-top:22px;font-size:6px;font-weight:700;color:var(--red)}
.news-title{margin-top:8px;font-size:6.4px;font-weight:700;color:var(--navy);line-height:11px}
.news-text{margin-top:7px;font-size:5.2px;color:var(--muted);line-height:11px}

/* footer */
.footer{position:absolute;left:0;top:1081px;width:699px;height:119px;background:var(--navy);color:var(--white);text-align:center}
.footer-brand{position:absolute;top:20px;width:100%;font-size:17px;font-weight:700}
.social{position:absolute;top:53px;left:0;width:100%;display:flex;justify-content:center;gap:3px}
.social span{width:11px;height:11px;border-radius:50%;background:#8a89c0}
.footer-nav{position:absolute;top:76px;width:100%;font-size:6.4px;color:#e6e6f2;word-spacing:2px}
.footer-nav i{font-style:normal;margin:0 7px}
.copyright{position:absolute;top:98px;width:100%;font-size:6.2px;color:#e6e6f2}
</style>
</head>
<body>
<div class="page">

  <header class="hero">
    <div class="hero-photo" role="img" aria-label="Speaker at a podium in front of flags"></div>
    <div class="brand">Lantern Boards</div>
    <nav class="nav">
      <a class="active" href="#" style="left:301px">Home</a>
      <a href="#" style="left:348px">Business</a>
      <a href="#" style="left:407px">Politics</a>
      <a href="#" style="left:460px">Entertainment</a>
      <a href="#" style="left:545px">Social Issues</a>
    </nav>
    <svg class="arrow" style="left:48px" viewBox="0 0 14 16"><path d="M10 2 L4 8 L10 14" stroke="#fff" stroke-width="2.2" fill="none"/></svg>
    <svg class="arrow" style="left:638px" viewBox="0 0 14 16"><path d="M4 2 L10 8 L4 14" stroke="#fff" stroke-width="2.2" fill="none"/></svg>
    <div class="search">
      <div class="search-field">Search Your Subject</div>
      <div class="search-btn">SEARCH NOW</div>
    </div>
  </header>

  <h2 class="section-title" style="top:359px">OUR CATEGORIES</h2>

  <div class="card" style="left:102px">
    <div class="card-photo" role="img" aria-label="Hands typing on a laptop" style="background:linear-gradient(135deg,#6f7c8c,#c9d0d8)"></div>
    <div class="card-title"><svg viewBox="0 0 8 8"><path d="M0 8H8M1 7V3M3 7V1M5 7V4M7 7V2" stroke="#2f2e66" stroke-width="1.2"/></svg>Business</div>
    <ul class="bullets"><li>Sed ut perspiciatis unde</li><li>Omnis iste natus</li><li>Error sit voluptatem</li><li>Accusantium</li></ul>
  </div>
  <div class="card" style="left:229px">
    <div class="card-photo" role="img" aria-label="Speaker at a press conference with microphones" style="background:linear-gradient(180deg,#1d2246,#5a5f7c 70%,#c9c4c8)"></div>
    <div class="card-title"><svg viewBox="0 0 8 8"><rect x="2.5" y="0" width="3" height="5" rx="1.5" fill="#2f2e66"/><path d="M1.5 4a2.5 2.5 0 0 0 5 0M4 6.5V8" stroke="#2f2e66" fill="none"/></svg>Politics</div>
    <ul class="bullets"><li>Sed ut perspiciatis unde</li><li>Omnis iste natus</li><li>Error sit voluptatem</li><li>Accusantium</li></ul>
  </div>
  <div class="card" style="left:356px">
    <div class="card-photo" role="img" aria-label="Microphone on stage under colourful lights" style="background:radial-gradient(circle at 40% 40%,#8a4a5a,#2a1c3a 60%,#14142a)"></div>
    <div class="card-title"><svg viewBox="0 0 8 8"><path d="M0 3H2L6 1V7L2 5H0Z" fill="#2f2e66"/></svg>Entertainment</div>
    <ul class="bullets"><li>Sed ut perspiciatis unde</li><li>Omnis iste natus</li><li>Error sit voluptatem</li><li>Accusantium</li></ul>
  </div>
  <div class="card" style="left:483px">
    <div class="card-photo" role="img" aria-label="Crowd at an evening street gathering" style="background:linear-gradient(180deg,#2a3358,#8a6a5a 60%,#3a2a2a)"></div>
    <div class="card-title"><svg viewBox="0 0 8 8"><ellipse cx="3.5" cy="3" rx="3.5" ry="2.5" fill="#2f2e66"/><path d="M1 5L0.5 7.5L3 5.3Z" fill="#2f2e66"/></svg>Social Issues</div>
    <ul class="bullets"><li>Sed ut perspiciatis unde</li><li>Omnis iste natus</li><li>Error sit voluptatem</li><li>Accusantium</li></ul>
  </div>

  <div class="band popular">MOST POPULAR LINKS</div>
  <div class="band recent">RECENT LINKS</div>
  <div class="links">
    <ul class="bullets" style="left:102px"><li>Sed ut perspiciatis unde</li><li>Omnis iste natus</li><li>Error sit voluptatem</li><li>Accusantium</li><li>Sed ut perspiciatis unde</li><li>Omnis iste natus</li></ul>
    <ul class="bullets" style="left:226px"><li>Sed ut perspiciatis unde</li><li>Omnis iste natus</li><li>Error sit voluptatem</li><li>Accusantium</li><li>Perspiciatis unde</li><li>Omnis iste</li></ul>
    <ul class="bullets" style="left:357px"><li>Sed ut perspiciatis unde</li><li>Omnis iste natus</li><li>Error sit voluptatem</li><li>Accusantium</li><li>Sed ut perspiciatis unde</li><li>Omnis</li></ul>
    <ul class="bullets" style="left:480px"><li>Sed ut perspiciatis unde</li><li>Omnis iste natus</li><li>Error sit voluptatem</li><li>Accusantium</li><li>Perspiciatis unde</li><li>Omnis iste</li></ul>
  </div>

  <h2 class="section-title" style="top:808px">FEATURED NEWS</h2>

  <article class="news" style="left:102px">
    <div class="news-photo" role="img" aria-label="Audience listening to a speaker in warm light" style="background:linear-gradient(120deg,#2a1a14,#8a5a30 55%,#1a1410)"></div>
    <div class="news-date">JULY 22nd 2016</div>
    <div class="news-title">Sed ut perspiciatis unde omnis<br>iste natus error sit accusant</div>
    <p class="news-text">Sed ut perspiciatis unde omnis iste natus error sit voluptatem accusantium doloremque laudantium, totam rem aperiam, eaque ipsa quae ab illo inventore veritatis et quasi architecto</p>
  </article>
  <article class="news" style="left:272px">
    <div class="news-photo" role="img" aria-label="Concert crowd under fireworks" style="background:linear-gradient(180deg,#3a1a4a,#a04a8a 45%,#2a1430)"></div>
    <div class="news-date">JULY 22nd 2016</div>
    <div class="news-title">Sed ut perspiciatis unde omnis<br>iste natus error sit accusant</div>
    <p class="news-text">Sed ut perspiciatis unde omnis iste natus error sit voluptatem accusantium doloremque laudantium, totam rem aperiam, eaque ipsa quae ab illo inventore veritatis et quasi architecto</p>
  </article>
  <article class="news" style="left:442px">
    <div class="news-photo" role="img" aria-label="Couple enjoying a film in a cinema" style="background:linear-gradient(90deg,#8a2a2a,#c8a07a 50%,#b03030)"></div>
    <div class="news-date">JULY 22nd 2016</div>
    <div class="news-title">Sed ut perspiciatis unde omnis<br>iste natus error sit accusant</div>
    <p class="news-text">Sed ut perspiciatis unde omnis iste natus error sit voluptatem accusantium doloremque laudantium, totam rem aperiam, eaque ipsa quae ab illo inventore veritatis et quasi architecto</p>
  </article>

  <footer class="footer">
    <div class="footer-brand">Lantern Boards</div>
    <div class="social" aria-label="Social links"><span></span><span></span><span></span><span></span><span></span><span></span><span></span></div>
    <div class="footer-nav">Home<i>|</i>Business<i>|</i>Politics<i>|</i>Entertainment<i>|</i>Social Issues</div>
    <div class="copyright">© 2016 Company Name &nbsp;| All Rights Reserved</div>
  </footer>

</div>
</body>
</html>
```